Bluewater Getaways KT needs a new Website

We have an old website that is just that - old. We need a fresh website that is professional graphic designed that has the following features.
1. Can be updated by ourselves in some areas.
2. Has a shopping cart.
3. Has links to download PDF files
4. Has links to other pages in the website
5. Includes social media links
6. Has a client log-in area
Full details in brief provided.

SORRY BUT IT'S URGENT. We've taken too long to write the details and it is now urgent. So my apologies I will be asking for designers to work quickly.

We will continue to use our existing web hosting company and url. Their is a link to the old website in the Design Brief.
Updates

UPDATE:  Please see the new file UPDATE TO DESIGN BRIEF.
Thanks for all your submissions to date.  We hope the update will assist with your designs.
As indicated in previous messages, we are happy with the Home Page + 1 Page in order to select the designer to work with in creating the full design. 

Thankyou Designers.  Much appreciate your efforts.
It's getting late here on Norfolk so I won't have much chance too review any more designs this evening.
But for your information:
Designer 7318405 Ravindra Mehta is so far the closest to what we are seeking.
Thanks again. 

Reason: Have extended to Monday 7 October to give time for designers to submit after feedback today. Especially given the time differences

Target Market(s)

Very wide audience. Current client group not that tech savvy, but we hope to broaden our market and sell more creative products, and so website needs to consider how people now use media, ie tablets & iphones.

Industry/Entity Type

Shopping

Requirements
Nice to have
• PLEASE SEE THE "UPDATE TO THE DESIGN BRIEF"

```html
<!DOCTYPE html>
<html lang="en">
<head>
<meta charset="utf-8">
<title>Bluewater Getaways KT – Home</title>
<link rel="stylesheet" href="https://fonts.googleapis.com/css2?family=Open+Sans:wght@400;600;700;800&family=Kaushan+Script&display=swap">
<style>
:root{
  --green:#1daa4f;
  --green-line:#3fbf6a;
  --orange:#f58220;
  --white:#ffffff;
  --ink:#333333;
  --cream:#f3e6a2;
  --cream-deep:#e6cf72;
}
*{box-sizing:border-box;margin:0;padding:0}
html,body{width:1200px;height:700px;overflow:hidden;background:#fff}
body{font-family:"Open Sans",sans-serif;color:var(--white)}
.page{position:relative;width:1200px;height:700px;overflow:hidden}

/* left navigation */
.sidebar{position:absolute;left:0;top:0;width:233px;height:700px;background:var(--green)}
.brand{position:absolute;left:0;top:0;width:233px;height:128px;background:var(--white)}
.brand-zigzag{position:absolute;left:0;top:122px}
.brand-name{position:absolute;left:22px;top:46px;display:flex;align-items:center;gap:9px;color:var(--orange);font-weight:700;font-size:17px;line-height:1.1}
.brand-dot{width:22px;height:22px;border-radius:50%;background:var(--orange);flex:none}
.nav{position:absolute;left:0;top:152px;width:233px;list-style:none}
.nav li{height:40px;display:flex;align-items:center;border-bottom:1px solid var(--green-line);font-size:13px;line-height:16px}
.nav li.is-active{background:var(--orange);border-bottom-color:var(--orange)}
.nav-icon{width:67px;display:flex;justify-content:center;flex:none}
.btn{position:absolute;display:flex;align-items:center;gap:12px;background:var(--orange);color:var(--white);font-size:18px;padding-left:12px}
.btn-book{left:32px;top:644px;width:157px;height:40px}

/* orange column */
.enterprise{position:absolute;left:233px;top:0;width:255px;height:700px;background:var(--orange)}
.enterprise-title{position:absolute;left:32px;top:26px;font-weight:800;font-size:31px;line-height:31px}
.enterprise-est{position:absolute;left:31px;top:92px;font-size:19px}
.script{font-family:"Kaushan Script",cursive;font-weight:400}
.supported{position:absolute;left:20px;top:180px;font-size:34px}
.tick-list{position:absolute;left:42px;top:244px;list-style:none}
.tick-list li{height:28px;display:flex;align-items:center;gap:9px;font-size:20px}
.enterprise-intro{position:absolute;left:18px;top:412px;width:230px;font-size:15px;line-height:19px}
.need-list{position:absolute;left:40px;top:481px;list-style:none}
.need-list li{display:flex;gap:9px;align-items:flex-start;font-size:15px;line-height:17px;margin-bottom:7px}
.need-list svg{margin-top:4px;flex:none}

/* main */
.hero{position:absolute;left:488px;top:0;width:544px;height:700px}
.hero-bg{position:absolute;inset:0;background:radial-gradient(ellipse at 30% 30%,#f8eeb8 0%,var(--cream) 45%,var(--cream-deep) 100%)}
.promotes{position:absolute;left:72px;top:46px;font-size:36px;color:var(--ink)}
.hero-title{position:absolute;left:16px;top:126px;width:544px;text-align:center;color:var(--ink);font-weight:800;font-size:47px;line-height:60px}
.slider{position:absolute;left:26px;top:377px;width:488px;height:273px;background:linear-gradient(160deg,#9ab26a 0%,#6d8a4a 45%,#b9a98a 100%);box-shadow:0 2px 6px rgba(0,0,0,.25)}
.slider-arrow{position:absolute;top:126px}
.slider-dots{position:absolute;left:236px;top:254px;display:flex;gap:5px}
.slider-dots span{width:8px;height:8px;border-radius:50%;background:var(--white)}
.slider-dots span.is-current{background:var(--orange)}

/* right column */
.aside{position:absolute;left:1032px;top:0;width:168px;height:700px;background:var(--green);text-align:center}
.aside-head{background:var(--orange);font-weight:700;font-size:15px;line-height:19px;display:flex;align-items:center;justify-content:center}
.head-contacts{height:70px}
.contact{font-size:10.3px;line-height:12.5px}
.contact-icon{display:block;margin:0 auto 3px}
.head-media{position:absolute;left:0;top:392px;width:168px;height:42px}
.media{position:absolute;left:0;top:444px;width:168px;font-size:10.3px;line-height:12.8px}
.media u{text-decoration:underline}
.support-title{position:absolute;left:0;top:566px;width:168px;font-weight:700;font-size:15px}
.shop-art{position:absolute;left:18px;top:588px;width:100px;height:56px;background:linear-gradient(120deg,#f5a04a,#e8e2d8 55%,#3a3f4a);border-radius:4px}
.btn-shop{left:14px;top:654px;width:136px;height:36px;font-size:18px;gap:8px}
</style>
</head>
<body>
<div class="page">

  <aside class="sidebar">
    <div class="brand">
      <div class="brand-name"><span class="brand-dot"></span>Bluewater<br>Getaways KT</div>
    </div>
    <svg class="brand-zigzag" width="233" height="12" viewBox="0 0 233 12"><path d="M0 0 H233 V6 L228 12 L223 6 L218 12 L213 6 L208 12 L203 6 L198 12 L193 6 L188 12 L183 6 L178 12 L173 6 L168 12 L163 6 L158 12 L153 6 L148 12 L143 6 L138 12 L133 6 L128 12 L123 6 L118 12 L113 6 L108 12 L103 6 L98 12 L93 6 L88 12 L83 6 L78 12 L73 6 L68 12 L63 6 L58 12 L53 6 L48 12 L43 6 L38 12 L33 6 L28 12 L23 6 L18 12 L13 6 L8 12 L3 6 L0 9 Z" fill="#fff"/></svg>

    <ul class="nav">
      <li class="is-active"><span class="nav-icon"><svg width="22" height="20" viewBox="0 0 22 20"><path d="M11 1 L21 10 H18 V19 H13 V13 H9 V19 H4 V10 H1 Z" fill="#fff"/></svg></span>Home</li>
      <li><span class="nav-icon"><svg width="18" height="20" viewBox="0 0 18 20"><rect x="2" y="2" width="14" height="17" fill="none" stroke="#fff" stroke-width="2"/><path d="M6 6h2M10 6h2M6 10h2M10 10h2M6 14h2M10 14h2" stroke="#fff" stroke-width="2"/></svg></span>Governance</li>
      <li><span class="nav-icon"><svg width="22" height="22" viewBox="0 0 22 22"><path d="M3 20 H19" stroke="#fff" stroke-width="2"/><path d="M11 20 L13 6" stroke="#fff" stroke-width="2"/><path d="M13 6 L7 4 M13 6 L18 3 M13 6 L19 9" stroke="#fff" stroke-width="2"/></svg></span>Norfolk Island</li>
      <li><span class="nav-icon"><svg width="20" height="20" viewBox="0 0 20 20"><rect x="2" y="2" width="12" height="16" fill="none" stroke="#fff" stroke-width="2"/><circle cx="13" cy="12" r="4" fill="none" stroke="#fff" stroke-width="2"/><path d="M16 15 L19 18" stroke="#fff" stroke-width="2"/></svg></span>Our Mission<br>and Values</li>
      <li><span class="nav-icon"><svg width="20" height="22" viewBox="0 0 20 22"><rect x="2" y="3" width="12" height="16" fill="none" stroke="#fff" stroke-width="2"/><circle cx="14" cy="16" r="5" fill="#fff"/><path d="M11.5 16 L13.5 18 L17 14" stroke="#1daa4f" stroke-width="1.6" fill="none"/></svg></span>Services</li>
      <li><span class="nav-icon"><svg width="20" height="22" viewBox="0 0 20 22"><circle cx="10" cy="6" r="4" fill="#fff"/><path d="M2 20 Q10 8 18 20 Z" fill="#fff"/></svg></span>Our Facilitator</li>
      <li><span class="nav-icon"><svg width="22" height="20" viewBox="0 0 22 20"><rect x="1" y="1" width="20" height="6" fill="#fff"/><path d="M3 8 V19 H19 V8" fill="none" stroke="#fff" stroke-width="2"/><rect x="8" y="12" width="6" height="7" fill="#fff"/></svg></span>Our Shop</li>
      <li><span class="nav-icon"><svg width="24" height="18" viewBox="0 0 24 18"><circle cx="6" cy="5" r="3" fill="#fff"/><circle cx="12" cy="4" r="3" fill="#fff"/><circle cx="18" cy="5" r="3" fill="#fff"/><path d="M1 16 Q6 7 11 16 Z M7 16 Q12 6 17 16 Z M13 16 Q18 7 23 16 Z" fill="#fff"/></svg></span>Holiday Programs</li>
      <li><span class="nav-icon"><svg width="18" height="22" viewBox="0 0 18 22"><path d="M3 10 H15 L13 21 H5 Z" fill="#fff"/><path d="M6 10 L4 2 M9 10 V1 M12 10 L15 3" stroke="#fff" stroke-width="2"/></svg></span>Design your own<br>Norfolk Island Holiday</li>
      <li><span class="nav-icon"><svg width="22" height="20" viewBox="0 0 22 20"><circle cx="11" cy="4" r="3" fill="#fff"/><circle cx="4" cy="16" r="3" fill="#fff"/><circle cx="18" cy="16" r="3" fill="#fff"/><path d="M11 4 V11 L4 16 M11 11 L18 16" stroke="#fff" stroke-width="1.6"/></svg></span>Kaleido Creative Projects</li>
      <li><span class="nav-icon"><svg width="24" height="22" viewBox="0 0 24 22"><circle cx="7" cy="4" r="3" fill="#fff"/><circle cx="17" cy="5" r="2.5" fill="#fff"/><path d="M7 8 V21 M3 2 L7 11 L11 2 M17 9 V21 M14 13 H20" stroke="#fff" stroke-width="2.4"/></svg></span>Schoolies, Siblings &amp;<br>and Family Holidays</li>
      <li><span class="nav-icon"><svg width="22" height="16" viewBox="0 0 22 16"><ellipse cx="11" cy="7" rx="10" ry="6" fill="#fff"/><path d="M5 11 L3 16 L10 12 Z" fill="#fff"/></svg></span>Testimonials</li>
    </ul>

    <div class="btn btn-book"><svg width="22" height="24" viewBox="0 0 22 24"><circle cx="11" cy="6" r="5" fill="#fff"/><path d="M4 14 H18 V19 H4 Z M2 21 H20 V23 H2 Z" fill="#fff"/></svg>Book Now</div>
  </aside>

  <section class="enterprise">
    <h1 class="enterprise-title">Our SOCIAL<br>ENTERPRISE</h1>
    <p class="enterprise-est">Established July 2001</p>
    <p class="supported script">Supported</p>
    <ul class="tick-list">
      <li><svg width="16" height="14" viewBox="0 0 16 14"><path d="M1 8 L6 13 L15 1" stroke="#fff" stroke-width="3" fill="none"/></svg>holidays</li>
      <li><svg width="16" height="14" viewBox="0 0 16 14"><path d="M1 8 L6 13 L15 1" stroke="#fff" stroke-width="3" fill="none"/></svg>travel</li>
      <li><svg width="16" height="14" viewBox="0 0 16 14"><path d="M1 8 L6 13 L15 1" stroke="#fff" stroke-width="3" fill="none"/></svg>recreation</li>
      <li><svg width="16" height="14" viewBox="0 0 16 14"><path d="M1 8 L6 13 L15 1" stroke="#fff" stroke-width="3" fill="none"/></svg>respite</li>
      <li><svg width="16" height="14" viewBox="0 0 16 14"><path d="M1 8 L6 13 L15 1" stroke="#fff" stroke-width="3" fill="none"/></svg>creative projects</li>
    </ul>
    <p class="enterprise-intro">for people requiring support to participate in socially inclusive events.</p>
    <ul class="need-list">
      <li><svg width="10" height="10" viewBox="0 0 10 10"><circle cx="5" cy="5" r="4.5" fill="#fff"/></svg>Intellectual Disability</li>
      <li><svg width="10" height="10" viewBox="0 0 10 10"><circle cx="5" cy="5" r="4.5" fill="#fff"/></svg>Acquired Brain Injury</li>
      <li><svg width="10" height="10" viewBox="0 0 10 10"><circle cx="5" cy="5" r="4.5" fill="#fff"/></svg>Mental Health</li>
      <li><svg width="10" height="10" viewBox="0 0 10 10"><circle cx="5" cy="5" r="4.5" fill="#fff"/></svg>Sensory Impairment</li>
      <li><svg width="10" height="10" viewBox="0 0 10 10"><circle cx="5" cy="5" r="4.5" fill="#fff"/></svg>Frail Aged</li>
      <li><svg width="10" height="10" viewBox="0 0 10 10"><circle cx="5" cy="5" r="4.5" fill="#fff"/></svg>Mobility Challenged</li>
      <li><svg width="10" height="10" viewBox="0 0 10 10"><circle cx="5" cy="5" r="4.5" fill="#fff"/></svg>Siblings of children with<br>Disabilities</li>
    </ul>
  </section>

  <main class="hero">
    <div class="hero-bg" role="img" aria-label="Faint pale-yellow photograph of island pine trees"></div>
    <p class="promotes script">Promotes</p>
    <h2 class="hero-title">Diversity Caring<br>Community<br>Norfolk Island</h2>
    <div class="slider" role="img" aria-label="Photo slide: a cheerful group of holiday guests waving their hands at a park picnic table">
      <svg class="slider-arrow" style="left:8px" width="14" height="22" viewBox="0 0 14 22"><path d="M12 2 L3 11 L12 20" stroke="#fff" stroke-width="3" fill="none"/></svg>
      <svg class="slider-arrow" style="right:8px" width="14" height="22" viewBox="0 0 14 22"><path d="M2 2 L11 11 L2 20" stroke="#fff" stroke-width="3" fill="none"/></svg>
      <div class="slider-dots"><span></span><span></span><span class="is-current"></span></div>
    </div>
  </main>

  <aside class="aside">
    <div class="aside-head head-contacts">LOCATION<br>AND CONTACTS</div>
    <div class="contact" style="margin-top:12px">
      <svg class="contact-icon" width="18" height="18" viewBox="0 0 18 18"><circle cx="9" cy="9" r="9" fill="#fff"/><path d="M9 4 a3.5 3.5 0 0 1 3.5 3.5 C12.5 10 9 14 9 14 S5.5 10 5.5 7.5 A3.5 3.5 0 0 1 9 4Z" fill="#1daa4f"/><circle cx="9" cy="7.5" r="1.3" fill="#fff"/></svg>
      Harbour Lane, Cove Point<br>PO Box 517<br>Norfolk Island NSW 2898<br>SOUTH PACIFIC<br>N.B.N. 415 702 386
    </div>
    <div class="contact" style="margin-top:8px">
      <svg class="contact-icon" width="18" height="18" viewBox="0 0 18 18"><circle cx="9" cy="9" r="9" fill="#fff"/><path d="M6 4 L8 7 L7 8 Q8 10.5 10 11 L11 10 L14 12 L12.5 14 Q6 13 4.5 6 Z" fill="#1daa4f"/></svg>
      International + 67 23 58194<br>Australia 1800 462 318<br>New Zealand
    </div>
    <div class="contact" style="margin-top:9px">
      <svg class="contact-icon" width="18" height="18" viewBox="0 0 18 18"><circle cx="9" cy="9" r="9" fill="#fff"/><rect x="4.5" y="5.5" width="9" height="7" fill="none" stroke="#1daa4f" stroke-width="1.3"/><path d="M4.5 5.5 L9 9.5 L13.5 5.5" stroke="#1daa4f" stroke-width="1.3" fill="none"/></svg>
      hello@bluewatergetaways.org
    </div>
    <div class="contact" style="margin-top:9px">
      <svg class="contact-icon" width="18" height="18" viewBox="0 0 18 18"><circle cx="9" cy="9" r="9" fill="#fff"/><circle cx="9" cy="9" r="5" fill="none" stroke="#1daa4f" stroke-width="1.2"/><path d="M4 9 H14 M9 4 Q6 9 9 14 Q12 9 9 4" stroke="#1daa4f" stroke-width="1.1" fill="none"/></svg>
      www.bluewatergetaways.org
    </div>
    <div class="contact" style="margin-top:9px">
      <svg class="contact-icon" width="18" height="18" viewBox="0 0 18 18"><circle cx="9" cy="9" r="9" fill="#fff"/><circle cx="9" cy="9" r="3" fill="#1daa4f"/></svg>
      www.friendspace.com/<br>bluewatergetaways
    </div>

    <div class="aside-head head-media">IMAGES &amp; VIDEO</div>
    <div class="media">
      <svg width="22" height="20" viewBox="0 0 22 20"><rect x="2" y="5" width="18" height="13" rx="1" fill="none" stroke="#fff" stroke-width="2"/><path d="M7 1 L11 5 L15 1" stroke="#fff" stroke-width="1.6" fill="none"/><path d="M9 8 L14 11.5 L9 15 Z" fill="#fff"/></svg>
      <p style="margin-top:2px"><u>BLUEWATER VIDEO</u> to see<br>more photographs and video's<br><u>FOLLOW</u> our FRIENDSPACE page</p>
      <p style="margin-top:9px"><u>CLIENT LOGIN</u><br><u>Kaleido Film Festival</u></p>
    </div>
    <p class="support-title">SUPPORT US</p>
    <div class="shop-art" role="img" aria-label="Shop merchandise: brochures, a t-shirt, a hat and a drink bottle"></div>
    <div class="btn btn-shop"><svg width="20" height="20" viewBox="0 0 22 20"><rect x="1" y="1" width="20" height="6" fill="#fff"/><path d="M3 8 V19 H19 V8" fill="none" stroke="#fff" stroke-width="2"/><rect x="8" y="12" width="6" height="7" fill="#fff"/></svg>Our Shop</div>
  </aside>

</div>
</body>
</html>
```